kestrelnet9 - a safety solution for schools

A Amok App for schools needs your help to design some screens. Its important to have a very simple use of the app. The function of the app is very easy, you put the button to trigger the alarm. The app has a message function. So we need 3 howto screens. you find a better description of the project in the briefing-file. If you have any questions just ask. Thanks in advance for the suggestions. Best Regards, Lars

Target Market(s)

Schools

Industry/Entity Type

Security Service

Font styles to use
Sans Serif

Colors

Designer to choose colors to be used in the design.

Requirements
Must have
• Simple, easy to use, look like a security app, trust,

```html
<!DOCTYPE html>
<html lang="de">
<head>
<meta charset="utf-8">
<title>kestrelnet9 – Startbildschirm</title>
<link rel="stylesheet" href="https://fonts.googleapis.com/css2?family=Oswald:wght@600&family=Roboto:wght@400;500&display=swap">
<style>
  :root {
    --page-bg: #ecebf3;
    --screen-top: #5a36c2;
    --screen-mid: #3b4fbb;
    --screen-bottom: #1d6cae;
    --text-light: #ffffff;
    --text-soft: rgba(255, 255, 255, 0.9);
    --decor-tint: rgba(90, 150, 230, 0.35);
  }
  * { box-sizing: border-box; margin: 0; padding: 0; }
  html, body {
    width: 1200px;
    height: 1200px;
    overflow: hidden;
    background: var(--page-bg);
  }
  .canvas {
    position: relative;
    width: 1200px;
    height: 1200px;
  }
  .splash-screen {
    position: absolute;
    left: 290px;
    top: 50px;
    width: 620px;
    height: 1100px;
    overflow: hidden;
    background: linear-gradient(200deg, var(--screen-top) 0%, var(--screen-mid) 50%, var(--screen-bottom) 100%);
    font-family: "Roboto", sans-serif;
    color: var(--text-light);
  }
  .security-backdrop {
    position: absolute;
    left: 0;
    top: 60px;
    width: 620px;
    height: 900px;
    background:
      radial-gradient(ellipse 200px 280px at 160px 420px, var(--decor-tint), transparent 75%),
      radial-gradient(ellipse 320px 400px at 380px 450px, rgba(120, 110, 220, 0.18), transparent 80%);
  }
  .status-bar {
    position: absolute;
    top: 14px;
    left: 10px;
    right: 10px;
    height: 22px;
    display: flex;
    align-items: center;
    justify-content: space-between;
    font-size: 18px;
    color: var(--text-light);
  }
  .status-left, .status-right {
    display: flex;
    align-items: center;
    gap: 8px;
    width: 200px;
  }
  .status-right { justify-content: flex-end; }
  .status-time { font-size: 18px; }
  .brand {
    position: absolute;
    left: 0;
    right: 0;
    top: 450px;
    text-align: center;
  }
  .brand-mark {
    display: block;
    width: 96px;
    height: 96px;
    margin: 0 auto 20px;
    border-radius: 50%;
    background: var(--text-light);
  }
  .brand-name {
    font-family: "Oswald", sans-serif;
    font-weight: 600;
    font-size: 58px;
    line-height: 1;
    letter-spacing: 0.5px;
    text-transform: uppercase;
    color: var(--text-light);
  }
  .brand-tagline {
    margin-top: 14px;
    font-size: 19px;
    color: var(--text-soft);
  }
  .app-version {
    position: absolute;
    left: 0;
    right: 0;
    top: 1032px;
    text-align: center;
    font-size: 18px;
    letter-spacing: 0.5px;
    color: var(--text-soft);
  }
</style>
</head>
<body>
<main class="canvas">
  <section class="splash-screen">
    <div class="security-backdrop" role="img" aria-label="Faint backdrop of a large shield with keyhole over rows of hexadecimal code"></div>

    <header class="status-bar">
      <div class="status-left">
        <svg width="52" height="12" viewBox="0 0 52 12" aria-hidden="true">
          <circle cx="5" cy="6" r="4.5" fill="#fff"/>
          <circle cx="15" cy="6" r="4.5" fill="#fff"/>
          <circle cx="25" cy="6" r="4.5" fill="#fff"/>
          <circle cx="35" cy="6" r="4" fill="none" stroke="#fff" stroke-width="1"/>
          <circle cx="45" cy="6" r="4" fill="none" stroke="#fff" stroke-width="1"/>
        </svg>
        <span>NOVA</span>
        <svg width="18" height="14" viewBox="0 0 18 14" aria-hidden="true">
          <path d="M1 5 A11 11 0 0 1 17 5" fill="none" stroke="#fff" stroke-width="2"/>
          <path d="M4 8 A7 7 0 0 1 14 8" fill="none" stroke="#fff" stroke-width="2"/>
          <circle cx="9" cy="12" r="1.8" fill="#fff"/>
        </svg>
      </div>
      <div class="status-time">4:21 PM</div>
      <div class="status-right">
        <svg width="10" height="18" viewBox="0 0 10 18" aria-hidden="true">
          <path d="M1 5 L9 13 L5 17 V1 L9 5 L1 13" fill="none" stroke="rgba(255,255,255,0.6)" stroke-width="1.3"/>
        </svg>
        <span>100%</span>
        <svg width="38" height="16" viewBox="0 0 38 16" aria-hidden="true">
          <rect x="0.5" y="1.5" width="33" height="13" rx="3" fill="none" stroke="#fff"/>
          <rect x="2.5" y="3.5" width="29" height="9" rx="1.5" fill="#fff"/>
          <rect x="35" y="5.5" width="2" height="5" rx="1" fill="#fff"/>
        </svg>
      </div>
    </header>

    <div class="brand">
      <span class="brand-mark"></span>
      <h1 class="brand-name">kestrelnet9</h1>
      <p class="brand-tagline">Weil Sicherheit immer zählt!</p>
    </div>

    <p class="app-version">v 0.0.1</p>
  </section>
</main>
</body>
</html>
```